Wellness Podcast Seeks Art work

This podcast is me telling my story of transformation through my life and travels. The tag line is: Conversations on self-esteem, self-confidence and transformation through a gay lense. My Lantern 7 bright.

I think I would like a logo/design I can use for artwork on the podcast with a cool font reading:

Lantern 7 Bright

I was thinking having a photo in the background that is of nature or something uplifting like you see on a lot of inspirational quotes with nature/mountains/sun in the background - but a design with the option to change the background picture for specific episodes maybe with a picture of myself for some.

I can provide some photos of me from a current trip to Bali I was on where I learned a lot of these lessons I wish to share.

I love anything with beach, or surf, or ocean, and that gives a yoga feel.

I will be discussing how to get to know yourself, through sharing my story and hopefully inspiring people to want to grow. Heavy self reflection and self-development, and positive mindset are what I would like to portray.

Target Market(s)

podcast listeners, spiritual seekers, people who seek change in their lives

Font styles to use
Serif
Sans Serif

Colors
33b8a4
87cfc6
85cae6
fbf289
0592cd
fbee3d
ffffff

Requirements
Must have
• Cool catchy font and style - with something unique that catches a listener's eye. It needs to stand out in podvale, but have an element of inspiration or beauty about it.
• Nice to have an element of gay content that people will gravitate toward but not that will push away other listeners
Nice to have
• some element of activity - like yoga, surf, or challenging your mind through activity -
• as that will be part of my podcast content.
• position on a photo that shows great font but shows something that creates curiosity in the potential listener
Should not have
• Nothing too hokey or esoteric.
• Not too busy looking as it will be in a small icon on some people's smart phones
• The photos I have attached below are not necessarily the ones I want used, unless you make it look really cool. They are more for you to get inspiration. One design has submitted has all the photos I added and I'm afraid it looks too busy.

```html
<!DOCTYPE html>
<html lang="en">
<head>
<meta charset="utf-8">
<title>Lantern 7 Bright – Podcast Cover</title>
<link rel="stylesheet" href="https://fonts.googleapis.com/css2?family=Comfortaa:wght@700&family=Roboto+Condensed:wght@300;400;700;900&display=swap">
<style>
  :root {
    --sky-top: #8e9fbb;
    --sky-mid: #b9c6d6;
    --horizon: #d3dbe4;
    --sea-deep: #2a5a7c;
    --sea-teal: #1f7f8c;
    --foliage: #2f5a22;
    --ink: #111111;
    --white: #ffffff;
  }
  * { margin: 0; padding: 0; box-sizing: border-box; }
  html, body { width: 1200px; height: 1200px; overflow: hidden; }
  .cover {
    position: relative;
    width: 1200px;
    height: 1200px;
    overflow: hidden;
  }
  .cover-photo {
    position: absolute;
    inset: 0;
    background:
      radial-gradient(ellipse 520px 620px at 260px 1000px, rgba(150,110,80,0.55), rgba(150,110,80,0) 70%),
      radial-gradient(ellipse 700px 420px at 1050px 920px, rgba(63,106,46,0.9), rgba(63,106,46,0) 75%),
      linear-gradient(180deg,
        var(--sky-top) 0%,
        var(--sky-mid) 28%,
        var(--horizon) 50%,
        var(--sea-deep) 58%,
        var(--sea-teal) 78%,
        var(--foliage) 100%);
  }
  .podcast-name {
    position: absolute;
    left: 0;
    top: 0;
    width: 1200px;
    height: 420px;
  }
  .podcast-name text {
    font-family: "Comfortaa", sans-serif;
    font-weight: 700;
    font-size: 150px;
    fill: var(--ink);
  }
  .tagline {
    position: absolute;
    right: 136px;
    top: 632px;
    width: 420px;
    text-align: right;
    color: var(--white);
    font-family: "Roboto Condensed", sans-serif;
    text-transform: uppercase;
  }
  .tagline .line { display: block; white-space: nowrap; }
  .tagline .bold { font-weight: 700; }
  .tagline .heavy { font-weight: 900; }
  .tagline .light { font-weight: 300; }
  .tagline .minor { font-size: 32px; font-weight: 400; }
  .line-conversations { font-size: 48px; line-height: 64px; }
  .line-esteem { font-size: 48px; line-height: 64px; }
  .line-confidence { font-size: 44px; line-height: 64px; }
  .line-and { font-size: 40px; line-height: 60px; letter-spacing: 14px; padding-right: 66px; }
  .line-transformation { font-size: 50px; line-height: 56px; }
  .line-through { font-size: 70px; line-height: 70px; }
  .line-through .minor { font-size: 56px; font-weight: 300; }
  .line-lense { font-size: 70px; line-height: 72px; }
</style>
</head>
<body>
<main class="cover">
  <div class="cover-photo" role="img" aria-label="Photo of the host taking a selfie on a clifftop above a turquoise bay and ocean, cloudy sky above and green foliage below"></div>

  <svg class="podcast-name" viewBox="0 0 1200 420" role="img" aria-label="Lantern 7 Bright">
    <text x="600" y="238" text-anchor="middle" textLength="720" lengthAdjust="spacingAndGlyphs">Lantern 7</text>
    <text x="600" y="356" text-anchor="middle" textLength="500" lengthAdjust="spacingAndGlyphs">Bright</text>
  </svg>

  <p class="tagline">
    <span class="line line-conversations bold">Conversations</span>
    <span class="line line-esteem bold"><span class="minor">On</span> Self-Esteem,</span>
    <span class="line line-confidence heavy">Self-Confidence</span>
    <span class="line line-and light">And</span>
    <span class="line line-transformation bold">Transformation</span>
    <span class="line line-through light">Through <span class="minor">A</span></span>
    <span class="line line-lense light">Gay Lense.</span>
  </p>
</main>
</body>
</html>
```